**Business Card**Designs Project** LornaTrade,LLC

Im looking for a simple and elegant Business Card that has a professional Corporate look and feel. Im considering a Metal business card as well as 2 color layout, Embossed, 1 color two tone layout(File#6 like).

The card should NOT be too busy but subtle. Clean look providing Key Details.

please see uploaded files for actual logo and inspirational design i like.

See Uploaded File # 3 for Professional Logos Style

Target Market(s)

investors

Industry/Entity Type

Business

Contact Information for Business Card

Side 1 information
Lorna Trade,LLC - Description Text below main logo = (Funding - Sales) or (Commercial - Residential) or (Property - Funding )
www.lornatrade-demo.com

Side 2 Information =
Dov Pelkin | Managing Broker
P 555-014-7781 | F 555-016-2490
E info@lornatrade-demo.com
membership logos - see file #3 for stye and file #4 for inspiration

Side 2 = 10pt Font
BRE: 07281944
NMLS: 6620573

Colors
3277b5
5c5c5c
333333
959595
85acd3
1b1b1b
ffffff

Requirements
Must have
• Lorna Trade, LLC **G Logo** - See Uploaded File #5 ,
• Contact Information - See Business Card Details Above
• Web address = www.lornatrade-demo.com
• Membership logos - See Uploaded File #4 & 9
Nice to have
• 1 Color two tones, grey, White, Charcoal Grey, Dark Turquois, Dark blue, Slate blue,
• GOOD COMBINATIONS: White and Grey, white and Charcoal grey with a splash of blue, Charcoal grey card with White, etc..
• PLEASE TRY DARK BLUE DESIGNS
• Embossed, card designs
• Metal Business card design
Should not have
• I DONT LIKE ALOTE OF WAVE DESIGNS

```html
<!DOCTYPE html>
<html lang="en">
<head>
<meta charset="utf-8">
<title>Lorna Trade, LLC — Business Card</title>
<link rel="stylesheet" href="https://fonts.googleapis.com/css2?family=Questrial&family=Source+Sans+3:wght@400&display=swap">
<style>
  :root {
    --page-bg: #ffffff;
    --card-bg: #666666;
    --card-shadow: rgba(0, 0, 0, 0.35);
    --ink-light: #f2f2f2;
    --ink-soft: #e6e6e6;
    --rule: #9a9a9a;
    --band-bg: #f1f1f1;
    --band-ink: #6a6a6a;
  }
  * { box-sizing: border-box; margin: 0; padding: 0; }
  html, body {
    width: 1017px; height: 1200px; overflow: hidden;
    background: var(--page-bg);
  }
  .canvas { position: relative; width: 1017px; height: 1200px; }

  .card {
    position: absolute; left: 185px; width: 645px; height: 368px;
    background: var(--card-bg);
    box-shadow: 8px 8px 8px var(--card-shadow);
    overflow: hidden;
    font-family: "Source Sans 3", sans-serif;
    color: var(--ink-light);
  }
  .card--front { top: 188px; }
  .card--back  { top: 667px; }

  /* brand lockup */
  .brand { position: absolute; display: flex; align-items: center; }
  .brand__dot { border-radius: 50%; background: var(--ink-light); flex: none; }
  .brand__divider { background: var(--ink-light); flex: none; }
  .brand__text { font-family: "Questrial", sans-serif; color: var(--ink-light); }
  .brand__name { display: block; white-space: nowrap; }
  .brand__tagline { display: block; white-space: nowrap; letter-spacing: 0.08em; }

  .card--front .brand { left: 45px; top: 127px; }
  .card--front .brand__dot { width: 46px; height: 46px; margin-right: 30px; }
  .card--front .brand__divider { width: 2px; height: 142px; margin-right: 20px; }
  .card--front .brand__name { font-size: 38px; line-height: 1; margin-bottom: 16px; }
  .card--front .brand__tagline { font-size: 20px; }

  .card--back .brand { left: 52px; top: 59px; }
  .card--back .brand__dot { width: 28px; height: 28px; margin-right: 24px; }
  .card--back .brand__divider { width: 2px; height: 86px; margin-right: 12px; }
  .card--back .brand__name { font-size: 23px; line-height: 1; margin-bottom: 10px; }
  .card--back .brand__tagline { font-size: 12.5px; }

  .website {
    position: absolute; right: 28px; bottom: 12px;
    font-size: 16px; letter-spacing: 0.01em;
  }

  .person { position: absolute; right: 45px; top: 172px; text-align: right; }
  .person__name { font-size: 29px; line-height: 1; }
  .person__role { font-size: 16px; line-height: 1; margin-top: 6px; }

  .divider-rule {
    position: absolute; left: 55px; top: 217px; width: 402px; height: 1px;
    background: var(--rule);
  }
  .address {
    position: absolute; left: 55px; top: 235px;
    font-size: 16.5px; line-height: 21px; color: var(--ink-soft);
    font-style: normal;
  }

  .contact-band {
    position: absolute; left: 0; top: 293px; width: 100%; height: 38px;
    background: var(--band-bg);
    display: flex; align-items: center;
    font-size: 16px; color: var(--band-ink);
  }
  .contact-band__item { position: absolute; display: flex; align-items: center; gap: 4px; }
  .contact-band__item svg { width: 16px; height: 16px; fill: none; stroke: var(--band-ink); stroke-width: 1.4; }
  .contact-band__item--phone { left: 58px; }
  .contact-band__item--fax { left: 222px; }
  .contact-band__item--email { left: 385px; }
</style>
</head>
<body>
<div class="canvas">

  <section class="card card--front" aria-label="Card front">
    <div class="brand">
      <span class="brand__dot"></span>
      <span class="brand__divider"></span>
      <div class="brand__text">
        <span class="brand__name">LORNA TRADE, LLC</span>
        <span class="brand__tagline">COMMERCIAL &amp; RESIDENTIAL</span>
      </div>
    </div>
    <p class="website">www.lornatrade-demo.com</p>
  </section>

  <section class="card card--back" aria-label="Card back">
    <div class="brand">
      <span class="brand__dot"></span>
      <span class="brand__divider"></span>
      <div class="brand__text">
        <span class="brand__name">LORNA TRADE, LLC</span>
        <span class="brand__tagline">COMMERCIAL &amp; RESIDENTIAL</span>
      </div>
    </div>

    <div class="person">
      <p class="person__name">Dov Pelkin</p>
      <p class="person__role">Managing Broker</p>
    </div>
    <div class="divider-rule"></div>
    <address class="address">2218 Meadow Park Drive Nashville,<br>TN 37299</address>

    <div class="contact-band">
      <span class="contact-band__item contact-band__item--phone">
        <svg viewBox="0 0 16 16" aria-hidden="true"><path d="M4 2 L6 2 L7 5 L5.5 6.5 Q7 9.5 9.5 10.5 L11 9 L14 10 L14 12 Q13 14 11 14 Q4 12 2 5 Q2 3 4 2 Z" fill="#6a6a6a"/></svg>
        555-014-7781
      </span>
      <span class="contact-band__item contact-band__item--fax">
        <svg viewBox="0 0 16 16" aria-hidden="true"><rect x="4" y="1.5" width="8" height="4"/><rect x="1.5" y="5.5" width="13" height="6" fill="#6a6a6a"/><rect x="4" y="9.5" width="8" height="5" fill="#f1f1f1"/></svg>
        555-016-2490
      </span>
      <span class="contact-band__item contact-band__item--email">
        <svg viewBox="0 0 18 16" aria-hidden="true" style="width:19px"><rect x="1" y="3" width="16" height="10"/><path d="M1 3 L9 9 L17 3"/></svg>
        info@lornatrade-demo.com
      </span>
    </div>
  </section>

</div>
</body>
</html>
```